Business Card Design

We are a Sydney based bespoke Concierge company, providing hospitality services including Concierge staffing, catering, home dining, events, delivery, stallorix, and manage desks in residential apartment services. Our website goes into more detail.

Target Market(s)

corporate clients, upscale residential clients, executives,

Industry/Entity Type

Hospitality

Contact Information for Business Card

David SouthwellDirector of Operations & Customer Experience
Marlowe Concierge
W:www.marloweconcierge-demo.net;
E;peter@marloweconcierge-demo.net
M: 0412 907 281

Font styles to use
Serif

Colors
3176b5
85cae6
d2a4cc
6b449b

Requirements
Must have
• Business name
• Name
• Title
• Tel
• Email
• Website
Nice to have
• Back - facebook , twitter, instagram

```html
<!DOCTYPE html>
<html lang="en">
<head>
<meta charset="utf-8">
<title>Marlowe Concierge – Business Card</title>
<link rel="stylesheet" href="https://fonts.googleapis.com/css2?family=PT+Sans:wght@400;700&display=swap">
<style>
  :root {
    --page-bg: #e9ebee;
    --card-white: #fbfbfb;
    --brand-blue: #3176b5;
    --brand-sky: #85cae6;
    --deep-blue: #1f6fb3;
    --bright-blue: #3aa3da;
    --text-grey: #5b6066;
    --rule-grey: #c9ced3;
  }
  * { box-sizing: border-box; margin: 0; padding: 0; }
  html, body { width: 1200px; height: 1062px; overflow: hidden; }
  body {
    background: var(--page-bg);
    font-family: "PT Sans", sans-serif;
    position: relative;
  }
  .card {
    position: absolute;
    left: 215px;
    width: 770px;
    height: 440px;
    border-radius: 4px;
    overflow: hidden;
    box-shadow: 0 8px 24px rgba(0,0,0,0.18);
  }
  /* Front */
  .card-front { top: 62px; background: var(--card-white); }
  .front-swoosh { position: absolute; inset: 0; width: 100%; height: 100%; }
  .brand-name {
    position: absolute;
    left: 70px;
    top: 140px;
    font-weight: 400;
    font-size: 46px;
    line-height: 0.95;
    letter-spacing: 1px;
    color: var(--brand-sky);
    text-transform: uppercase;
  }
  .divider {
    position: absolute;
    left: 382px;
    top: 112px;
    width: 1px;
    height: 120px;
    background: var(--rule-grey);
  }
  .person {
    position: absolute;
    left: 412px;
    top: 40px;
  }
  .person-name {
    font-weight: 700;
    font-size: 27px;
    color: var(--brand-blue);
  }
  .person-title {
    font-size: 15px;
    color: var(--text-grey);
    margin-top: 2px;
  }
  .contact {
    position: absolute;
    left: 412px;
    top: 116px;
    font-size: 17px;
    color: var(--text-grey);
    line-height: 1.45;
  }
  .address { margin-bottom: 12px; }
  .contact-line { display: flex; align-items: center; gap: 10px; }
  .contact-line svg { width: 15px; height: 15px; flex: none; }
  /* Back */
  .card-back {
    top: 560px;
    background: radial-gradient(ellipse at 55% 45%, var(--bright-blue) 0%, var(--deep-blue) 80%);
  }
  .back-brand {
    position: absolute;
    left: 90px;
    top: 120px;
    font-weight: 400;
    font-size: 96px;
    line-height: 0.92;
    letter-spacing: 2px;
    color: #ffffff;
    text-transform: uppercase;
  }
</style>
</head>
<body>

<section class="card card-front" aria-label="Card front">
  <svg class="front-swoosh" viewBox="0 0 770 440" preserveAspectRatio="none" aria-hidden="true">
    <defs>
      <linearGradient id="waveBlue" x1="0" y1="0" x2="1" y2="0">
        <stop offset="0" stop-color="#9fd3ee"/>
        <stop offset="0.5" stop-color="#3a9ad6"/>
        <stop offset="1" stop-color="#1f6fb3"/>
      </linearGradient>
    </defs>
    <path d="M0 440 L0 402 C250 406 460 388 590 335 C660 305 720 292 770 286 L770 440 Z" fill="url(#waveBlue)"/>
    <path d="M0 416 C260 420 480 404 610 355 C680 328 730 318 770 314" stroke="#ffffff" stroke-width="6" fill="none"/>
    <path d="M0 428 C270 432 500 418 630 372 C695 348 740 340 770 337" stroke="#cfe9f6" stroke-width="3" fill="none" opacity="0.8"/>
  </svg>

  <div class="brand-name">Marlowe<br>Concierge</div>
  <div class="divider"></div>

  <div class="person">
    <p class="person-name">Peter Hollingby</p>
    <p class="person-title">Director of Operations &amp; Customer Experience</p>
  </div>

  <div class="contact">
    <p class="address">H.NO48 Ferry Lane<br>block7 Harbourside</p>
    <p class="contact-line">
      <svg viewBox="0 0 16 16" aria-hidden="true"><path d="M4 1 L6.5 4 L5 6 C6 8.5 7.5 10 10 11 L12 9.5 L15 12 L13 15 C7 14.5 1.5 9 1 3 Z" fill="var(--brand-blue)"/></svg>
      0412 907 281
    </p>
    <p class="contact-line">
      <svg viewBox="0 0 16 16" aria-hidden="true"><circle cx="8" cy="8" r="7" fill="none" stroke="var(--brand-blue)" stroke-width="1.5"/><ellipse cx="8" cy="8" rx="3" ry="7" fill="none" stroke="var(--brand-blue)" stroke-width="1.2"/><line x1="1" y1="8" x2="15" y2="8" stroke="var(--brand-blue)" stroke-width="1.2"/></svg>
      www.marloweconcierge-demo.net
    </p>
    <p class="contact-line">
      <svg viewBox="0 0 16 16" aria-hidden="true"><text x="8" y="13" text-anchor="middle" font-family="PT Sans, sans-serif" font-weight="700" font-size="15" fill="var(--brand-blue)">@</text></svg>
      peter@marloweconcierge-demo.net
    </p>
  </div>
</section>

<section class="card card-back" aria-label="Card back">
  <div class="back-brand">Marlowe<br>Concierge</div>
</section>

</body>
</html>
```